Fahrzeugbeschriftung für Ambulante Krankenpflege
Zielgruppe
Ambulante Krankenpflege
Aufgabenstellung
Besonderer Wert: Gut Lesbar, Zeitlos und Modern
Text: Wir gehen den Weg mit Ihnen gemeinsam
Fahrzeug ZK Ilo Modell 2018

```html
<!DOCTYPE html>
<html lang="de">
<head>
<meta charset="utf-8">
<title>LUMA Ambulante Krankenpflege – Fahrzeugbeschriftung</title>
<link rel="stylesheet" href="https://fonts.googleapis.com/css2?family=Montserrat:wght@300;400;700&family=Yellowtail&display=swap">
<style>
  :root {
    --teal: #17a383;
    --ink: #1b1b1b;
    --paper: #ffffff;
    --backdrop: #f2f3f2;
    --photo-a: #7f9a6a;
    --photo-b: #c9b6a8;
  }
  * { margin: 0; padding: 0; box-sizing: border-box; }
  html, body { width: 1200px; height: 764px; overflow: hidden; background: var(--backdrop); }
  .livery { position: relative; width: 1200px; height: 764px; background: var(--paper); font-family: "Montserrat", sans-serif; color: var(--ink); }
  .livery-shapes { position: absolute; inset: 0; }
  .brand { position: absolute; left: 388px; top: 420px; }
  .brand-name { font-weight: 700; font-size: 36px; letter-spacing: 4px; color: var(--teal); line-height: 1; }
  .service { position: absolute; font-weight: 700; line-height: 1; white-space: nowrap; }
  .service-line1 { left: 536px; top: 400px; font-size: 19px; }
  .service-line2 { left: 547px; top: 423px; font-size: 17px; }
  .phone { position: absolute; left: 580px; top: 446px; font-weight: 300; font-size: 17px; white-space: nowrap; }
  .slogan { position: absolute; left: 386px; top: 488px; font-family: "Yellowtail", cursive; font-size: 22px; line-height: 1.2; color: var(--paper); white-space: nowrap; }
  .web { position: absolute; left: 414px; top: 541px; font-size: 12.5px; letter-spacing: 4.6px; color: var(--teal); white-space: nowrap; }
</style>
</head>
<body>
<div class="livery">
  <svg class="livery-shapes" width="1200" height="764" viewBox="0 0 1200 764">
    <defs>
      <linearGradient id="photoTone" x1="0" y1="0" x2="1" y2="1">
        <stop offset="0" stop-color="var(--photo-a)"/>
        <stop offset="1" stop-color="var(--photo-b)"/>
      </linearGradient>
    </defs>
    <polygon class="slogan-band" points="310,484 782,478 782,520 310,527" fill="var(--teal)"/>
    <polygon class="accent-lower" points="778,530 872,447 866,530" fill="var(--teal)"/>
    <polygon class="accent-upper" points="957,357 982,313 1007,313" fill="var(--teal)"/>
    <g role="img" aria-label="Foto: Pflegerin begleitet einen älteren Herrn im Freien">
      <polygon points="795,372 948,368 783,513" fill="url(#photoTone)" stroke="var(--teal)" stroke-width="4"/>
    </g>
    <g role="img" aria-label="Foto: Pflegerin und älterer Herr beim Spaziergang">
      <polygon points="882,437 1026,304 1011,433" fill="url(#photoTone)" stroke="var(--teal)" stroke-width="4"/>
    </g>
  </svg>

  <div class="brand">
    <span class="brand-name">LUMA</span>
  </div>
  <div class="service service-line1">AMBULANTE</div>
  <div class="service service-line2">KRANKENPFLEGE</div>
  <div class="phone">0 47 38 / 264 5100</div>
  <div class="slogan">Wir gehen den Weg mit Ihnen gemeinsam.</div>
  <div class="web">WWW.LUMA-PFLEGEDIENST.DE</div>
</div>
</body>
</html>
```